Flyer für haushaltsnahe Dienstleistungen für pflegebedürftige Personen
Zielgruppe
Wir bieten Haushaltsnahe Dienstleistungen für Pflegebedürftige Personen an.
Aufgabenstellung
Bestehenden Flyer den Inhalt aus angehängter Datei 'Sonnwacht Anzeige Zwiebel' kombinieren. Bedeutet den Inhalt:
'Verschenken Sie nicht Ihr Geld!!
Nutzen Sie Ihre Verhinderungspflege ab dem
Pflegegrad 2 bis zum 31.12.2023 sonst verfällt
diese. Denken Sie auch daran Ihren
Entlastungsbetrag ab Pflegegrad 1 zu nutzen.
Buchen Sie gleich ein Termin unter 0711 82 37
60 95 oder unter www.sonnwacht-muster.de. '
auf den neuen Flyer auf der ersten Seite unterbringen.
Vorhandenes Logo muß verwendet werden. Es sollte auch ein neues/anderes passendes Bild verwendet werden.
Vorhandene Adresse auf alten Flyer ersetzen in neue Adresse. Die neue Adresse lautet:
Firma Sonnwacht
Ottilie Brandauer
Lindenkamp 47
73712 Esslingen

```html
<!DOCTYPE html>
<html lang="de">
<head>
<meta charset="utf-8">
<title>Sonnwacht Flyer</title>
<link rel="stylesheet" href="https://fonts.googleapis.com/css2?family=Raleway:wght@400;500;800&family=Roboto:wght@700;900&family=Cinzel:wght@600&display=swap">
<style>
  :root {
    --red: #b8141f;
    --red-dark: #a50f1a;
    --ink: #3a3a3a;
    --paper: #f7f7f7;
    --page: #ffffff;
    --photo-blue: #2f5fa8;
    --photo-light: #dfe8f0;
    --photo-beige: #d9cbb4;
  }
  * { margin: 0; padding: 0; box-sizing: border-box; }
  html, body { width: 1200px; height: 1200px; overflow: hidden; background: var(--page); }
  .flyer {
    position: absolute; left: 346px; top: 69px; width: 507px; height: 1063px;
    background: var(--red); overflow: hidden; font-family: "Raleway", sans-serif;
  }
  .hero { position: absolute; left: 0; top: 0; width: 507px; height: 630px; }
  .hero-photo {
    position: absolute; inset: 0;
    background:
      linear-gradient(180deg, var(--paper) 0%, rgba(247,247,247,0.85) 14%, rgba(247,247,247,0) 40%),
      linear-gradient(100deg, var(--photo-blue) 0%, #5a82b8 30%, var(--photo-light) 48%, var(--photo-beige) 70%, #efe9df 100%);
  }
  .hero-curve { position: absolute; left: 0; top: 0; width: 507px; height: 630px; }
  .brand { position: absolute; left: 65px; top: 30px; display: flex; align-items: center; gap: 18px; }
  .brand-dot { width: 88px; height: 88px; border: 5px solid var(--red); border-radius: 50%; }
  .brand-name { font-family: "Cinzel", serif; font-weight: 600; font-size: 44px; color: var(--ink); letter-spacing: 1px; }
  .headline {
    position: absolute; right: 65px; top: 126px; text-align: right;
    font-family: "Roboto", sans-serif; font-weight: 900; font-size: 45px; line-height: 55px;
    color: var(--red); text-shadow: 2px 3px 4px rgba(0,0,0,0.25);
  }
  .subsidy {
    position: absolute; left: 294px; top: 448px; width: 213px; height: 146px;
    background: rgba(247,240,236,0.92); border-top-left-radius: 16px; border-bottom-left-radius: 16px;
    text-align: right; padding: 16px 32px 0 10px;
  }
  .subsidy-amount { font-weight: 800; font-size: 16.5px; line-height: 25px; color: var(--red); }
  .subsidy-note { margin-top: 9px; font-size: 13.5px; line-height: 18px; color: var(--ink); }
  .content { position: absolute; left: 65px; top: 630px; width: 400px; color: #fff; }
  .content-title { font-weight: 800; font-size: 21px; line-height: 26px; }
  .checklist { list-style: none; margin-top: 12px; }
  .checklist li { position: relative; padding-left: 27px; font-size: 17px; line-height: 24px; margin-bottom: 5px; }
  .checklist svg { position: absolute; left: 0; top: 5px; }
  .booking { margin-top: 26px; font-size: 18px; line-height: 24px; }
  .booking strong { font-weight: 800; }
  .address { position: absolute; left: 65px; top: 920px; color: #fff; font-size: 17px; line-height: 23px; }
  .address strong { font-weight: 800; }
  .email { position: absolute; right: 65px; top: 989px; color: #fff; font-size: 17px; line-height: 23px; white-space: nowrap; }
</style>
</head>
<body>
<div class="flyer">
  <div class="hero">
    <div class="hero-photo" role="img" aria-label="Foto: lächelnde Haushaltshilfe im blauen Poloshirt putzt mit Sprühflasche ein Fenster neben einem Vorhang"></div>
    <svg class="hero-curve" viewBox="0 0 507 630" aria-hidden="true">
      <path d="M0 617 Q 160 560 507 548 L507 630 L0 630 Z" fill="var(--red)"/>
      <path d="M0 605 Q 160 545 507 530 L507 548 Q 160 560 0 617 Z" fill="rgba(184,20,31,0.25)"/>
    </svg>
    <div class="brand">
      <div class="brand-dot"></div>
      <div class="brand-name">SONNWACHT</div>
    </div>
    <h1 class="headline">Verschenken<br>Sie nicht<br>Ihr Geld!!</h1>
    <div class="subsidy">
      <div class="subsidy-amount">Mind. 125€ mtl.<br>für Haushalshilfe<br>ab Pflegegrad 1</div>
      <div class="subsidy-note">Abrechnung mit allen<br>Pflegekassen möglich.</div>
    </div>
  </div>
  <div class="content">
    <h2 class="content-title">Haushaltshilfe für Pflegebedürftige</h2>
    <ul class="checklist">
      <li><svg width="18" height="16" viewBox="0 0 18 16"><path d="M2 9 L7 14 L16 2" stroke="#fff" stroke-width="2.6" fill="none" stroke-linecap="round"/></svg>Nutzen Sie Ihre Verhinderungspflege<br>ab dem Pflegegrad 2 bis zum 31.12.2023<br>sonst verfällt diese.</li>
      <li><svg width="18" height="16" viewBox="0 0 18 16"><path d="M2 9 L7 14 L16 2" stroke="#fff" stroke-width="2.6" fill="none" stroke-linecap="round"/></svg>Denken Sie auch daran Ihren Entlastungs-<br>betrag ab Pflegegrad 1 zu nutzen.</li>
    </ul>
    <p class="booking">Buchen Sie gleich ein Termin<br>unter <strong>Telefon 0711 82 37 60 95</strong> oder<br>unter <strong>www.sonnwacht-muster.de</strong></p>
  </div>
  <div class="address">
    <strong>Firma Sonnwacht</strong><br>Ottilie Brandauer<br>Lindenkamp 47<br>73712 Esslingen
  </div>
  <div class="email">E-mail: info@sonnwacht.de</div>
</div>
</body>
</html>
```